Business Card Design for a technology company

Our current business card is outdated and stale.

We need a new look and one soon.

We're a telematics (GPS tracking) company based in Australia. Our audiences are transport and logistics company.

Target Market(s)

1. Transport and Logistics Companies
2. Food and Beverage Manufacturers
3. Concrete Businesses

Industry/Entity Type

Logistics

Contact Information for Business Card

Lumen Rove

Font styles to use
Sans Serif

Colors
3276b5
0255a3
85acd3
cfdeed
ffffff

Requirements
Must have
• Logo
• "Premium Suppliers of Real Time Temperature Tracking"
• Contact Name
• Business Title
• Address
• Telephone
• Mobile
• Email
• Website URL
Nice to have
• Visual representation of tracking or maps.
Should not have
• Image of a satellite as currently shown

```html
<!DOCTYPE html>
<html lang="en">
<head>
<meta charset="utf-8">
<title>Lumen Rove Business Card</title>
<link rel="stylesheet" href="https://fonts.googleapis.com/css2?family=Questrial&family=Arimo:wght@400;700&display=swap">
<style>
  :root {
    --stage: #2a2a2c;
    --ink-dark: #060708;
    --brand-blue: #0255a3;
    --mid-blue: #3276b5;
    --soft-blue: #85acd3;
    --pale-blue: #cfdeed;
    --white: #ffffff;
    --text-dark: #1b1b1b;
  }
  * { margin: 0; padding: 0; box-sizing: border-box; }
  html, body { width: 1200px; height: 880px; overflow: hidden; }
  body { background: var(--stage); position: relative; font-family: "Arimo", Arial, sans-serif; }

  .card {
    position: absolute;
    width: 540px;
    height: 340px;
    border-radius: 22px;
    overflow: hidden;
    box-shadow: 0 18px 40px rgba(0,0,0,0.45);
  }

  /* Front */
  .card-front { left: 90px; top: 80px; background: var(--ink-dark); }
  .front-scene {
    position: absolute; left: 0; right: 0; bottom: 0; height: 230px;
    background:
      radial-gradient(ellipse 120% 100% at 70% 110%, #5f8fcf 0%, #2f5f9e 40%, #12305e 70%, rgba(6,7,8,0) 100%);
  }
  .front-brand {
    position: absolute; left: 44px; top: 70px;
    font-family: "Questrial", Arial, sans-serif;
    font-size: 64px; letter-spacing: -1px;
    color: var(--white);
  }
  .front-tagline {
    position: absolute; left: 0; right: 0; bottom: 42px; height: 44px;
    background: rgba(20,22,26,0.55);
    display: flex; align-items: center; justify-content: center;
    font-family: "Questrial", Arial, sans-serif;
    font-size: 19px; letter-spacing: 1px;
    color: var(--white);
  }

  /* Back */
  .card-back { left: 570px; top: 450px; background: var(--white); }
  .back-brand {
    position: absolute; left: 40px; top: 48px;
    font-family: "Questrial", Arial, sans-serif;
    font-size: 60px; letter-spacing: -1px;
    color: var(--brand-blue);
  }
  .back-address {
    position: absolute; right: 36px; top: 138px;
    text-align: right; font-size: 14px; line-height: 19px; color: var(--text-dark);
  }
  .back-address .web-name { color: var(--brand-blue); }
  .divider-main {
    position: absolute; left: 40px; right: 36px; top: 200px; height: 2px;
    background: var(--brand-blue);
  }
  .person { position: absolute; left: 40px; top: 215px; }
  .person-name { font-size: 20px; font-weight: 700; color: var(--brand-blue); line-height: 22px; }
  .person-title { font-size: 15px; color: var(--text-dark); line-height: 18px; }
  .divider-person {
    position: absolute; left: 40px; width: 200px; top: 262px; height: 2px;
    background: var(--mid-blue);
  }
  .contacts { position: absolute; left: 40px; top: 272px; list-style: none; }
  .contacts li {
    display: flex; align-items: center; gap: 8px;
    font-size: 14px; line-height: 19px; color: var(--text-dark);
  }
  .contacts svg { width: 14px; height: 14px; fill: var(--brand-blue); flex: none; }
</style>
</head>
<body>

  <section class="card card-front" aria-label="Card front">
    <div class="front-scene" role="img" aria-label="Photograph of Earth seen from orbit with blue cloud cover"></div>
    <div class="front-brand">Lumen Rove</div>
    <div class="front-tagline">Premium Suppliers of Real Time Temperature Tracking</div>
  </section>

  <section class="card card-back" aria-label="Card back">
    <div class="back-brand">Lumen Rove</div>
    <address class="back-address" style="font-style:normal">
      Unit 4, 18 Carrow Street Ferndale<br>
      VIC 3199 Australia<br>
      www.<span class="web-name">lumenrove</span>.com.au
    </address>
    <div class="divider-main"></div>
    <div class="person">
      <div class="person-name">Owen Harlow</div>
      <div class="person-title">Manager</div>
    </div>
    <div class="divider-person"></div>
    <ul class="contacts">
      <li>
        <svg viewBox="0 0 16 16" aria-hidden="true"><path d="M3 1h3l1.5 4-2 1.2a9 9 0 0 0 4.3 4.3L11 8.5l4 1.5v3a2 2 0 0 1-2 2A13 13 0 0 1 1 3a2 2 0 0 1 2-2z"/></svg>
        +03 1800 555 014
      </li>
      <li>
        <svg viewBox="0 0 16 16" aria-hidden="true"><rect x="4" y="1" width="8" height="14" rx="1.5"/><rect x="5.5" y="3" width="5" height="8" fill="#fff"/></svg>
        +03 1800 555 014
      </li>
      <li>
        <svg viewBox="0 0 16 16" aria-hidden="true"><rect x="1" y="3" width="14" height="10" rx="1"/><path d="M1.5 3.5 8 9l6.5-5.5" fill="none" stroke="#fff" stroke-width="1.3"/></svg>
        sales@lumenrove.com.au
      </li>
    </ul>
  </section>

</body>
</html>
```